Sponsor at Title Insurance Industry Seminar for Continuing Ed - 250 Companies in Attendance

I offer escrow accounting services in the Title Insurance Industry. I've attached logo files and an example of my former company. I don't like the design and it's a little wordy but it provides detail of what I offer.

Below is a brief write-up...
For professionals in the title insurance industry, finding a reliable and cost-effective solution to escrow accounting needs can feel overwhelming. When choosing the right accounting partner, title companies and law firms need a group they can trust, and that’s where we come in. Brightfern Ledger Solutions is a team that understands the title industry and the importance of compliance, security and accuracy. Brightfern Ledger Solutions is the experienced, convenient and cost-effective choice for the accounting and certification needs of companies throughout the country.

```html
<!DOCTYPE html>
<html lang="en">
<head>
<meta charset="utf-8">
<title>Brightfern Ledger Solutions – Escrow Reconciliation Flyer</title>
<link rel="stylesheet" href="https://fonts.googleapis.com/css2?family=Poppins:wght@300;400;600;700&family=Roboto:wght@400;500;700&display=swap">
<style>
  :root{
    --navy:#37404e;
    --clay:#bd7563;
    --white:#ffffff;
    --ink:#2f3540;
    --body:#4a4f57;
    --stage:#c0c0c0;
  }
  *{margin:0;padding:0;box-sizing:border-box}
  html,body{width:1200px;height:851px;overflow:hidden;background:var(--stage)}
  body{position:relative;font-family:"Roboto",Arial,sans-serif;color:var(--ink)}

  .page{position:absolute;top:52px;width:527px;height:746px;overflow:hidden;background:var(--white)}
  .page--front{left:46px}
  .page--back{left:618px}

  .photo{position:absolute;inset:0}
  .photo--accountant{background:linear-gradient(125deg,#d9dee2 0%,#eef0ee 35%,#b7c3d9 55%,#8fa3c8 68%,#e6e7e9 85%,#cfd3d6 100%)}
  .photo--advisor{background:linear-gradient(140deg,#eef1f1 0%,#e4e8e8 30%,#53698c 55%,#2d3f5e 65%,#dfe5ec 80%,#f2f3f3 100%)}

  .shapes{position:absolute;inset:0;width:100%;height:100%}

  .brand{position:absolute;left:26px;top:36px;display:flex;align-items:center;gap:6px;color:var(--white);font-family:"Poppins",Arial,sans-serif}
  .brand__mark{width:24px;height:24px;border:2px solid var(--white)}
  .brand__name{font-size:17px;font-weight:400;line-height:17px;letter-spacing:.3px}
  .brand__sub{font-size:7.5px;font-weight:400;letter-spacing:1px;line-height:9px;display:block}

  .headline{position:absolute;left:26px;top:152px;font-family:"Poppins",Arial,sans-serif;font-size:32px;line-height:37px;color:var(--white);font-weight:400;letter-spacing:-.3px}
  .headline__accent{color:var(--clay);font-weight:700;letter-spacing:-.8px;display:block}
  .headline__rule{position:absolute;left:26px;top:275px;width:50px;height:4px;background:var(--clay)}

  .year{position:absolute;left:156px;top:338px;width:100px;text-align:center;color:var(--white);font-family:"Poppins",Arial,sans-serif}
  .year__label{font-size:15px;line-height:18px;font-weight:400}
  .year__num{font-size:25px;line-height:28px;font-weight:700;letter-spacing:2px}

  .services-title{position:absolute;left:102px;top:464px;font-family:"Poppins",Arial,sans-serif;font-size:20px;letter-spacing:2.4px;color:var(--navy);font-weight:400}
  .services-title b{color:var(--clay);font-weight:700}

  .service{position:absolute;left:100px;display:flex;gap:10px}
  .service__icon{width:34px;height:34px;border-radius:50%;background:var(--navy);flex:none;display:flex;align-items:center;justify-content:center;margin-top:5px}
  .service__title{font-size:12.5px;font-weight:500;color:var(--clay);letter-spacing:.4px;line-height:15px}
  .service__text{font-size:8.3px;line-height:9.8px;color:var(--ink);margin-top:2px}

  .about-title{position:absolute;left:355px;top:348px;font-family:"Poppins",Arial,sans-serif;font-size:40px;line-height:42px;color:var(--white);font-weight:400;letter-spacing:-.5px}
  .about-rule{position:absolute;left:358px;top:443px;width:49px;height:4px;background:var(--white)}
  .about-text{position:absolute;left:58px;top:489px;width:280px;font-size:7.7px;line-height:10.7px;color:var(--body)}

  .promise{position:absolute;left:134px;display:flex;align-items:center;gap:9px}
  .promise__icon{width:28px;height:28px;border-radius:50%;background:var(--clay);display:flex;align-items:center;justify-content:center}
  .promise__label{font-size:11px;font-weight:700;color:var(--body)}

  .social{position:absolute;left:32px;top:686px;display:flex;gap:2px}
  .social__dot{width:21px;height:21px;border-radius:50%;border:1px solid var(--navy)}
  .website{position:absolute;left:34px;top:713px;font-size:8.4px;letter-spacing:1.1px;color:var(--ink)}
  .divider{position:absolute;left:209px;top:681px;width:2px;height:40px;background:var(--clay)}
  .contact{position:absolute;right:161px;top:673px;text-align:right;color:var(--ink)}
  .contact__address{font-size:8.4px;line-height:10.5px;letter-spacing:.5px}
  .contact__phone{font-size:10.5px;font-weight:500;letter-spacing:1px;margin-top:9px}
  .contact__icons{position:absolute;left:376px;top:673px;width:16px;height:50px}
</style>
</head>
<body>

<!-- FRONT PAGE -->
<section class="page page--front">
  <div class="photo photo--accountant" role="img" aria-label="Photo of an accountant at a desk working with a calculator and a binder of records"></div>
  <svg class="shapes" viewBox="0 0 1006 1423" preserveAspectRatio="none" aria-hidden="true">
    <polygon fill="#ffffff" points="393,560 863,1140 746,1258 870,1258 736,1395 608,1395 580,1423 0,1423 0,953"/>
    <polygon fill="#37404e" fill-opacity=".97" points="0,0 300,0 654,355 68,942 0,875"/>
    <polygon fill="#bd7563" points="393,559 520,685 393,811 266,685"/>
    <polygon fill="#bd7563" points="746,1258 1006,995 1006,1423 580,1423 608,1395 736,1395 870,1258"/>
  </svg>

  <div class="brand">
    <span class="brand__mark"></span>
    <div class="brand__name">BRIGHTFERN<span class="brand__sub">LEDGER SOLUTIONS</span></div>
  </div>

  <h1 class="headline">ESCROW<span class="headline__accent">RECONCILIATION</span>SERVICES</h1>
  <div class="headline__rule"></div>

  <div class="year">
    <div class="year__label">THIS YEAR</div>
    <div class="year__num">2024</div>
  </div>

  <h2 class="services-title">WHAT WE <b>DO</b></h2>

  <div class="service" style="top:498px">
    <div class="service__icon">
      <svg width="16" height="16" viewBox="0 0 16 16" fill="#fff"><rect x="2" y="9" width="2" height="5"/><rect x="5.5" y="7" width="2" height="7"/><rect x="9" y="9" width="2" height="5"/><rect x="12.5" y="5" width="2" height="9"/><path d="M2 7 L6 3.5 L9 6 L13 2" stroke="#fff" stroke-width="1.4" fill="none"/></svg>
    </div>
    <div>
      <div class="service__title">LOREM IPSUM</div>
      <p class="service__text">Lorem ipsum dolor sit amet, consectetur<br>adipiscing elit, sed do eiusmod tempor</p>
    </div>
  </div>

  <div class="service" style="top:554px">
    <div class="service__icon">
      <svg width="16" height="16" viewBox="0 0 16 16" fill="#fff"><rect x="1.5" y="4.5" width="13" height="9" rx="1.5"/><rect x="5.5" y="2" width="5" height="3" rx=".8" fill="none" stroke="#fff" stroke-width="1.2"/><rect x="1.5" y="8" width="13" height="1" fill="#37404e"/></svg>
    </div>
    <div>
      <div class="service__title">LOREM IPSUM</div>
      <p class="service__text">Lorem ipsum dolor sit amet, consectetur<br>adipiscing elit, sed do eiusmod tempor</p>
    </div>
  </div>

  <div class="service" style="top:612px">
    <div class="service__icon">
      <svg width="16" height="16" viewBox="0 0 16 16" fill="none" stroke="#fff" stroke-width="1.2"><rect x="2" y="4" width="6" height="10"/><rect x="8" y="1.5" width="6" height="12.5"/><path d="M3.5 7h3M3.5 9.5h3M10 11V8M12 11V5"/></svg>
    </div>
    <div>
      <div class="service__title">LOREM IPSUM</div>
      <p class="service__text">Lorem ipsum dolor sit amet, consectetur<br>adipiscing elit, sed do eiusmod tempor</p>
    </div>
  </div>

  <div class="social"><span class="social__dot"></span><span class="social__dot"></span><span class="social__dot"></span></div>
  <div class="website">WWW.COMPANYNAME.COM</div>
  <div class="divider"></div>
  <div class="contact">
    <p class="contact__address">123,Lorem ipsum dolor<br>amet consectetur</p>
    <p class="contact__phone">+1 888 888 8888</p>
  </div>
  <svg class="contact__icons" viewBox="0 0 16 50" aria-hidden="true">
    <path d="M8 2a5 5 0 0 0-5 5c0 4 5 9 5 9s5-5 5-9a5 5 0 0 0-5-5z" fill="#bd7563"/><circle cx="8" cy="7" r="2" fill="#fff"/>
    <path d="M3 32c1-1 2-1 3 0l1 2c0 1-1 1.5-1 2 1 2 2 3 4 4 .5 0 1-1 2-1l2 1c1 1 1 2 0 3-1 1-3 2-6 0-3-2-5-4-6-7-1-2 0-3 1-4z" fill="#bd7563"/>
  </svg>
</section>

<!-- BACK PAGE -->
<section class="page page--back">
  <div class="photo photo--advisor" role="img" aria-label="Photo of a consultant in a suit working at a desk in a bright office"></div>
  <svg class="shapes" viewBox="0 0 1006 1423" preserveAspectRatio="none" aria-hidden="true">
    <polygon fill="#37404e" points="0,278 360,638 0,993"/>
    <polygon fill="#ffffff" points="360,635 920,1197 695,1423 0,1423 0,993"/>
    <polygon fill="#bd7563" points="1006,295 515,785 1006,1283"/>
    <polygon fill="#37404e" points="695,1423 920,1197 1006,1283 1006,1423"/>
  </svg>

  <h2 class="about-title">WHO<br>WE ARE</h2>
  <div class="about-rule"></div>

  <p class="about-text">Lorem ipsum dolor sit amet, consectetur adipiscing elit, sed do eiusmod tempor incididunt ut labore et dolore magna aliqua. Ut enim ad minim veniam, quis nostrud exercitation ullamco laboris nisi ut aliquip ex ea commodo consequat. Duis aute irure dolor in reprehenderit in voluptate velit esse cillum dolore eu fugiat nulla pariatur. Excepteur sint occaecat cupidatat non proident, sunt in culpa qui officia deserunt mollit anim id est laborum.</p>

  <div class="promise" style="top:562px">
    <div class="promise__icon"><svg width="14" height="14" viewBox="0 0 14 14" fill="none" stroke="#fff" stroke-width="1.2"><path d="M3 1.5h6l2.5 2.5v8.5H3z"/><path d="M5 5.5h4M5 7.5h4M5 9.5h2"/></svg></div>
    <span class="promise__label">100% Compliance</span>
  </div>
  <div class="promise" style="top:595px">
    <div class="promise__icon"><svg width="14" height="14" viewBox="0 0 14 14" fill="none" stroke="#fff" stroke-width="1.2"><circle cx="7" cy="6" r="4"/><path d="M5.2 6l1.3 1.3 2.4-2.5"/></svg></div>
    <span class="promise__label">100% Convenience</span>
  </div>
  <div class="promise" style="top:628px">
    <div class="promise__icon"><svg width="14" height="14" viewBox="0 0 14 14" fill="none" stroke="#fff" stroke-width="1.2"><path d="M7 1.5l4.5 1.8v3.5c0 3-2 4.8-4.5 5.7C4.5 11.6 2.5 9.8 2.5 6.8V3.3z"/><path d="M5.2 7l1.3 1.3 2.4-2.5"/></svg></div>
    <span class="promise__label">100% Credibility</span>
  </div>

  <div class="social"><span class="social__dot"></span><span class="social__dot"></span><span class="social__dot"></span></div>
  <div class="website">WWW.COMPANYNAME.COM</div>
  <div class="divider"></div>
  <div class="contact">
    <p class="contact__address">123,Lorem ipsum dolor<br>amet consectetur</p>
    <p class="contact__phone">+1 888 888 8888</p>
  </div>
  <svg class="contact__icons" viewBox="0 0 16 50" aria-hidden="true">
    <path d="M8 2a5 5 0 0 0-5 5c0 4 5 9 5 9s5-5 5-9a5 5 0 0 0-5-5z" fill="#bd7563"/><circle cx="8" cy="7" r="2" fill="#fff"/>
    <path d="M3 32c1-1 2-1 3 0l1 2c0 1-1 1.5-1 2 1 2 2 3 4 4 .5 0 1-1 2-1l2 1c1 1 1 2 0 3-1 1-3 2-6 0-3-2-5-4-6-7-1-2 0-3 1-4z" fill="#bd7563"/>
  </svg>
</section>

</body>
</html>
```